BG & PSKB Tradeshow Backdrop Display

Backdrop Specs:
Size: 10ft wide x 10ft tall (Corvana Level Display)
Shape: Flat back wall
Full-color dye-sublimation print

Goal:
Create a high-impact backdrop showcasing the partnership between Bramblo Glow and Pine Sparkle Kit Brothers. Design should attract attention from across the trade show floor, clearly explain what we offer, and reflect professionalism, holiday spirit, and partnership.

Content to Include:
Logos for two brands, placed prominently and equally and a picture of Dale Morrow (owner of PineSparkleKitBrothers "PSKB") and Raymond Fisk (owner of Bramblo Glow "BG")

Headline (example):
“Nearly 50 Years of Combined Experience – Top-Tier Training & Industry-Leading Support”
or
“We Cover Everything: Training • Marketing • Products • Support”

Key Offerings (can be icons or short bullet list):
Rebate Programs
Hands-On Training
Sales & Marketing Support
Online Training Platform
Product Advancement Program
Operations & Team Management
Wholesale Pricing on Lighting & Décor

Imagery:
Training group photos, team member images, and festive lighting visuals.
Include PSKB elf mascot if it fits.
Dale (PSKB) is the photo of the man who has a beard.
Raymond (BG) is the photo of the man who is in a tan jacket
I included 3 circular images of a Bramblo Glow logo - this is our training logo. Please use only one that you feel will look the best on the design. We do not need all three.

Style & Colors:
Use each brand’s colors but make them blend harmoniously.
Festive holiday elements (twinkling lights, snowflakes, bokeh) as accents, not overpowering.
Professional yet approachable — balance fun (PSKB) with wholesale/training authority (Bramblo Glow, BGT).
Bramblo Glow branding colors: #0072bb (primary), #f59426 (secondary)
PineSparkleKitBrothers branding colors: #e82520 (primary), #1f6c39 (secondary)
Looking for a modern design.

Design Notes:
Keep text readable from 10–15 feet away.
Place key content at/above eye level for visibility.
Leave lower portion cleaner for booth furniture in front.
Background can subtly fade to highlight text and logos.

References Provided:
Partnership flyer (text, logos, photo ideas, color inspiration)
Kivo Stands example (format and proportions)

Target Market(s)

Entrepreneurs

Industry/Entity Type

Wholesale & Distribution

Colors
0054AA
0677BA
7BADD7
CADEEF
E8F1F8
00AB8E
00BBA5
67D7C9
C6EFE9
E9F9F6
FFC000
F8CF3A
FAE287
FDF2CF
FEFAEE
EB3D1F
EC4F4E
F09395
F8D3D4
FCEDEE

Requirements
Must have
• A modern feel with Christmas vibes entangling the two brands.
Nice to have
• Fun Christmas decor like snowflakes, snow, or other common Christmas theme decor - maybe Santa with a sleigh?
Should not have
• Nothing exact

```html
<!DOCTYPE html>
<html lang="en">
<head>
<meta charset="utf-8">
<title>BG &amp; PSKB Tradeshow Backdrop</title>
<link href="https://fonts.googleapis.com/css2?family=Roboto+Condensed:wght@300;400;700&display=swap" rel="stylesheet">
<style>
  :root {
    --stage: #e4e4e4;
    --paper: #ffffff;
    --navy: #2a2676;
    --navy-deep: #1e1a5c;
    --headline-blue: #2f5da8;
    --deep-red: #8c1a1a;
    --gold: #f5b120;
    --ink: #1f2a5a;
    --white: #ffffff;
  }
  * { box-sizing: border-box; margin: 0; padding: 0; }
  html, body { width: 1200px; height: 960px; overflow: hidden; }
  body {
    background: var(--stage);
    font-family: "Roboto Condensed", "Arial Narrow", sans-serif;
    position: relative;
  }
  .backdrop {
    position: absolute;
    left: 100px; top: 30px;
    width: 1000px; height: 900px;
    background: var(--paper);
    overflow: hidden;
    box-shadow: 0 4px 18px rgba(0,0,0,.12);
  }

  /* Left column: partnership message */
  .headline {
    position: absolute; left: 60px; top: 190px; width: 500px;
    text-align: center; color: var(--headline-blue);
    font-weight: 300; font-size: 50px; line-height: 1.12; text-transform: uppercase;
  }
  .subhead {
    position: absolute; left: 60px; top: 325px; width: 500px;
    text-align: center; color: var(--deep-red);
    font-weight: 700; font-size: 22px; line-height: 1.25; text-transform: uppercase;
  }
  .owner {
    position: absolute; top: 410px; width: 220px; text-align: center;
  }
  .owner--pskb { left: 100px; }
  .owner--bg { left: 310px; }
  .owner-portrait {
    display: block; margin: 0 auto;
    width: 104px; height: 104px; border-radius: 50%;
    border: 4px solid var(--gold);
  }
  .owner--pskb .owner-portrait { background: radial-gradient(circle at 50% 40%, #b88a6e, #7a4a3a 70%, #c23a2e); }
  .owner--bg .owner-portrait { background: radial-gradient(circle at 50% 40%, #d9b59a, #4e6f9a 75%); }
  .brand-name {
    margin-top: 26px; font-weight: 700; font-size: 24px; line-height: 1.1;
  }
  .owner--pskb .brand-name { color: #e82520; }
  .owner--bg .brand-name { color: #0072bb; }

  .coverage {
    position: absolute; left: 60px; top: 770px; width: 500px; text-align: center; color: var(--ink);
  }
  .coverage-title { font-weight: 700; font-size: 22px; text-transform: uppercase; }
  .coverage-list { font-size: 15px; letter-spacing: .5px; text-transform: uppercase; margin-top: 2px; }
  .training-badge {
    display: block; margin: 18px auto 0;
    width: 34px; height: 34px; border-radius: 50%;
    background: #0072bb; border: 3px solid var(--gold);
  }

  /* Right column: offerings band */
  .offer-band {
    position: absolute; left: 620px; top: 0; width: 300px; height: 900px;
    background: linear-gradient(180deg, var(--navy-deep) 0%, var(--navy) 30%, var(--navy) 100%);
  }
  .lights-strip {
    position: absolute; left: 620px; top: 0; width: 300px; height: 130px;
    background:
      radial-gradient(circle at 20% 55%, rgba(255,240,200,.55), transparent 12%),
      radial-gradient(circle at 55% 45%, rgba(255,240,200,.5), transparent 10%),
      radial-gradient(circle at 82% 60%, rgba(255,240,200,.5), transparent 11%),
      radial-gradient(circle at 40% 85%, rgba(190,70,170,.45), transparent 22%),
      linear-gradient(180deg, #3a2f8e, #2a2676);
  }
  .photo { position: absolute; }
  .photo--house-one { left: 604px; top: 160px; width: 148px; height: 112px; background: linear-gradient(160deg, #1d3a22, #c9a24a 60%, #3a5a2a); }
  .photo--house-two { left: 760px; top: 160px; width: 148px; height: 112px; background: linear-gradient(160deg, #1a1f38, #b8303a 55%, #2f8a5a); }
  .photo--team-one { left: 585px; top: 555px; width: 186px; height: 148px; background: linear-gradient(170deg, #6f8a5a, #c2443a 55%, #4e7a38); }
  .photo--team-two { left: 778px; top: 540px; width: 172px; height: 140px; background: linear-gradient(170deg, #9bb7d8, #b43a3a 50%, #4a5570); }

  .bracket { position: absolute; width: 22px; height: 40px; border: 0 solid var(--gold); }
  .bracket--house-one { left: 598px; top: 240px; border-left-width: 6px; border-bottom-width: 6px; }
  .bracket--house-two { left: 894px; top: 154px; border-right-width: 6px; border-top-width: 6px; }
  .bracket--team-one { left: 579px; top: 549px; border-left-width: 6px; border-top-width: 6px; }
  .bracket--team-two { left: 934px; top: 640px; border-right-width: 6px; border-bottom-width: 6px; }

  .offer-title {
    position: absolute; left: 640px; top: 318px; width: 270px;
    color: #d8dcf2; font-weight: 300; font-size: 38px; text-transform: uppercase;
  }
  .offer-list {
    position: absolute; left: 642px; top: 382px; width: 270px;
    list-style: none; color: var(--white);
    font-weight: 700; font-size: 14.5px; line-height: 22px; text-transform: uppercase;
  }
  .offer-list li { position: relative; padding-left: 16px; white-space: nowrap; }
  .offer-list li::before {
    content: ""; position: absolute; left: 0; top: 7px;
    width: 8px; height: 8px; border-radius: 50%; background: var(--gold);
  }
</style>
</head>
<body>
  <main class="backdrop">
    <h1 class="headline">Nearly 50 years of<br>combined experience</h1>
    <p class="subhead">Top-tier training &amp;<br>industry-leading support</p>

    <div class="owner owner--pskb">
      <span class="owner-portrait" role="img" aria-label="Portrait of Dale Morrow, owner of Pine Sparkle Kit Brothers"></span>
      <p class="brand-name">Pine Sparkle Kit Brothers</p>
    </div>
    <div class="owner owner--bg">
      <span class="owner-portrait" role="img" aria-label="Portrait of Raymond Fisk, owner of Bramblo Glow"></span>
      <p class="brand-name">Bramblo Glow</p>
    </div>

    <div class="coverage">
      <p class="coverage-title">We cover everything</p>
      <p class="coverage-list">Training • Marketing • Products • Support</p>
      <span class="training-badge" role="img" aria-label="Training program badge"></span>
    </div>

    <div class="offer-band"></div>
    <div class="lights-strip" role="img" aria-label="Festive string lights with soft bokeh"></div>

    <div class="photo photo--house-one" role="img" aria-label="Home decorated with warm holiday lights"></div>
    <div class="photo photo--house-two" role="img" aria-label="House lit with red and green holiday lights at night"></div>
    <span class="bracket bracket--house-one"></span>
    <span class="bracket bracket--house-two"></span>

    <h2 class="offer-title">Key offerings</h2>
    <ul class="offer-list">
      <li>Rebate programs</li>
      <li>Hands-on training</li>
      <li>Sales &amp; marketing support</li>
      <li>Online training platform</li>
      <li>Product advancement program</li>
      <li>Operations &amp; team management</li>
      <li>Wholesale pricing on lighting &amp; décor</li>
    </ul>

    <div class="photo photo--team-one" role="img" aria-label="Training group photo outdoors"></div>
    <div class="photo photo--team-two" role="img" aria-label="Team members gathered in front of a red building"></div>
    <span class="bracket bracket--team-one"></span>
    <span class="bracket bracket--team-two"></span>
  </main>
</body>
</html>
```